Verdant Rooms Stationary Set

Verdant Rooms is a bespoke interior design firm set to provide services to VIP clients with elegance and minimalism is the main theme for our stationary set. We require a full stationary set covering A4 letterhead, A4 & A3 envelopes, business cards, USB's, CDs, email signature and any other item the designer sees fit. logo is already designed and finalized, and we require the designer to use it as is without modifying the logo.

Address to be used on letterhead / business cards ...etc shall be as follows:

Phone : +971 2 518 3076
P.O. Box : 318947
Address: Block C&D, Bldg. 27, Court 14, Abu Dhabi, United Arab Emirates
Website: www.verdantrooms.example

Target Market(s)

VIP Clients

Industry/Entity Type

Interior Design

Font styles to use
Other font styles liked:
• something to be unique

Colors

Designer to choose colors to be used in the design.

Requirements
Must have
• Elegant, minimalistic
Nice to have
• Simple yet elegant design having a sharp yet clean cut format
Should not have
• No additional colours, just colours that are used in the logo (silver, black or gold)

```html
<!DOCTYPE html>
<html lang="en">
<head>
<meta charset="utf-8">
<title>Verdant Rooms – Business Card</title>
<link href="https://fonts.googleapis.com/css2?family=Cormorant+Garamond:wght@500&family=Cinzel:wght@400&family=Open+Sans:wght@400&display=swap" rel="stylesheet">
<style>
  :root {
    --backdrop: #dcdad6;
    --card-black: #0b0b0b;
    --card-white: #fbfbfa;
    --gold: #b9924c;
    --ink: #2b2b2b;
    --silver: #b8b8b8;
  }
  * { margin: 0; padding: 0; box-sizing: border-box; }
  html, body { width: 1200px; height: 908px; overflow: hidden; }
  body {
    background: var(--backdrop);
    position: relative;
    font-family: "Open Sans", Arial, sans-serif;
  }
  .card {
    position: absolute;
    width: 520px;
    height: 298px;
    box-shadow: 0 10px 24px rgba(0,0,0,0.18);
  }
  .card--front { left: 70px; top: 110px; background: var(--card-black); }
  .card--back  { left: 610px; top: 500px; background: var(--card-white); }

  .wordmark {
    font-family: "Cormorant Garamond", Georgia, serif;
    font-weight: 500;
    color: var(--gold);
    letter-spacing: 0.04em;
    white-space: nowrap;
  }
  .card--front .wordmark {
    position: absolute;
    left: 0; right: 0; top: 108px;
    text-align: center;
    font-size: 46px;
  }
  .card--front .web {
    position: absolute;
    left: 0; right: 0; top: 214px;
    text-align: center;
    font-size: 12px;
    letter-spacing: 0.05em;
    color: var(--silver);
  }
  .card--front .web span { color: var(--gold); }

  .card--back .wordmark {
    position: absolute;
    left: 28px; top: 110px;
    font-size: 30px;
  }
  .divider {
    position: absolute;
    left: 240px; top: 34px;
    width: 1px; height: 150px;
    background: var(--gold);
  }
  .person { position: absolute; left: 258px; top: 34px; }
  .person__name {
    font-family: "Cinzel", Georgia, serif;
    color: var(--gold);
    font-size: 19px;
    letter-spacing: 0.02em;
  }
  .person__role { font-size: 12.5px; color: var(--ink); margin-top: 2px; }
  .contacts { list-style: none; margin-top: 22px; }
  .contacts li {
    display: flex; align-items: center; gap: 7px;
    font-size: 12px; color: var(--ink); line-height: 19px;
  }
  .icon { width: 11px; height: 11px; flex: none; }
  .address {
    position: absolute;
    left: 28px; bottom: 30px;
    display: flex; align-items: center; gap: 7px;
    font-size: 12.5px; color: var(--ink);
  }
</style>
</head>
<body>

<section class="card card--front">
  <div class="wordmark">Verdant Rooms</div>
  <div class="web">www.<span>verdantrooms</span>.example</div>
</section>

<section class="card card--back">
  <div class="wordmark">Verdant Rooms</div>
  <div class="divider"></div>
  <div class="person">
    <div class="person__name">MARCUS HALE</div>
    <div class="person__role">Gerente General</div>
    <ul class="contacts">
      <li>
        <svg class="icon" viewBox="0 0 12 12"><circle cx="6" cy="6" r="6" fill="var(--gold)"/><path d="M4 3.2l1 1.3-.6.7c.4.9 1.1 1.6 2 2l.7-.6 1.3 1-.6 1.1C5.8 8.6 3.4 6.2 3 4z" fill="#fff"/></svg>
        +971 2 518 3076
      </li>
      <li>
        <svg class="icon" viewBox="0 0 12 12"><circle cx="6" cy="6" r="6" fill="var(--gold)"/><rect x="3" y="4" width="6" height="4.2" fill="none" stroke="#fff" stroke-width="0.9"/><path d="M3 4l3 2.3L9 4" fill="none" stroke="#fff" stroke-width="0.9"/></svg>
        info@verdantrooms.example
      </li>
      <li>
        <svg class="icon" viewBox="0 0 12 12"><circle cx="6" cy="6" r="6" fill="var(--gold)"/><circle cx="6" cy="6" r="3" fill="none" stroke="#fff" stroke-width="0.9"/><path d="M3 6h6M6 3c-1.3 1.6-1.3 4.4 0 6M6 3c1.3 1.6 1.3 4.4 0 6" fill="none" stroke="#fff" stroke-width="0.7"/></svg>
        www.verdantrooms.example
      </li>
    </ul>
  </div>
  <div class="address">
    <svg class="icon" viewBox="0 0 12 12"><circle cx="6" cy="6" r="6" fill="var(--gold)"/><path d="M6 9.5L3.8 6.2A2.3 2.3 0 1 1 8.2 6.2z" fill="#fff"/><circle cx="6" cy="5" r="0.9" fill="var(--gold)"/></svg>
    Block C&amp;D, Bldg. 27, Court 14, Abu Dhabi, United Arab Emirates
  </div>
</section>

</body>
</html>
```